Presentation Flyer for Married Couple at night separate business owners by day

I would like a flyer to use to advertise free presentations put on by husband and I. I (Danielle Vorhagen) am an estate planning attorney that works for PMR Law. My husband (Ray Vorhagen) is a financial planner that works for Belvorne Financial Planning. Would love it to be funny but serious. At night we are a married couple of 4 children, by day we individually work with people helping them protect their assets and their families.
Goal is for this to be used for multiple events.
Things to include: Food will be provided, Raffle for $500 off an Estate Plan Package
Topics to be covered in Seminar:
Estate & Financial Planning Essentials

Protect Your Future
Build a strong financial foundation with emergency funds, retirement planning, and smart investment strategies that match your goals.

Secure Your Legacy
Learn about wills, trusts, and powers of attorney - the essential documents everyone needs to protect their family's future.

Guard Your Assets
Understand the right insurance coverage to protect yourself and your loved ones, from life insurance to long-term care options.

Transfer Wealth Wisely
Discover tax-efficient strategies for passing assets to the next generation and making the most of your charitable giving.

```html
<!DOCTYPE html>
<html lang="en">
<head>
<meta charset="UTF-8">
<title>Estate &amp; Financial Planning Essentials</title>
<link rel="stylesheet" href="https://fonts.googleapis.com/css2?family=Montserrat:wght@100;200;400;500;600;700;800&display=swap">
<style>
  :root {
    --page-bg: #ece7e1;
    --brown-deep: #3a2716;
    --brown-tag: #4b3524;
    --brick-light: #c9a07a;
    --brick-mid: #a9784f;
    --ink-white: #ffffff;
    --ink-soft: rgba(255,255,255,0.85);
    --rule: rgba(255,255,255,0.45);
    --card-line: rgba(255,255,255,0.22);
    --icon-bg: #d9d3cd;
    --icon-ink: #4a3320;
  }
  * { box-sizing: border-box; margin: 0; padding: 0; }
  html, body { width: 1200px; height: 1200px; overflow: hidden; background: var(--page-bg); }
  body { font-family: "Montserrat", sans-serif; position: relative; }

  .flyer {
    position: absolute; left: 150px; top: 20px;
    width: 900px; height: 1160px;
    background: var(--brown-deep);
    overflow: hidden;
    box-shadow: 0 6px 24px rgba(0,0,0,0.18);
  }
  .hero-photo {
    position: absolute; inset: 0 0 auto 0; height: 720px;
    background:
      linear-gradient(180deg, rgba(58,39,22,0) 45%, rgba(58,39,22,0.75) 78%, var(--brown-deep) 100%),
      radial-gradient(ellipse 60% 55% at 52% 55%, #2d2a33 0%, #2d2a33 40%, rgba(45,42,51,0) 70%),
      linear-gradient(100deg, #d8cfc3 0%, var(--brick-light) 25%, var(--brick-mid) 60%, var(--brick-light) 85%, #d9b58f 100%);
  }
  .name-tag {
    position: absolute;
    background: var(--brown-tag);
    color: var(--ink-white);
    font-weight: 600; font-size: 19px;
    padding: 8px 30px 9px;
    border-radius: 20px;
    border: 1px solid rgba(255,255,255,0.35);
    white-space: nowrap;
  }
  .name-tag--left { left: 40px; top: 215px; }
  .name-tag--right { left: 655px; top: 320px; }
  .leaders { position: absolute; inset: 0; pointer-events: none; }

  .headline {
    position: absolute; left: 0; right: 0; top: 565px; text-align: center;
    color: var(--ink-white);
  }
  .headline__kicker { font-weight: 800; font-size: 34px; letter-spacing: 0.5px; line-height: 1.2; }
  .headline__main { font-weight: 100; font-size: 106px; line-height: 1.05; letter-spacing: 1px; }

  .perks {
    position: absolute; left: 120px; width: 660px; top: 725px;
    border-top: 1px solid var(--rule); border-bottom: 1px solid var(--rule);
    padding: 13px 0 12px;
    text-align: center; color: var(--ink-white);
    font-size: 15.5px; font-weight: 500; letter-spacing: 0.2px;
    white-space: nowrap;
  }

  .topics {
    position: absolute; left: 122px; top: 830px;
    display: flex; gap: 18px; align-items: stretch;
  }
  .topic {
    position: relative; width: 152px; min-height: 186px;
    border: 1px solid var(--card-line); border-radius: 6px;
    padding: 32px 9px 14px; text-align: center; color: var(--ink-white);
  }
  .topic__icon {
    position: absolute; top: -22px; left: 50%; transform: translateX(-50%);
    width: 44px; height: 44px; border-radius: 50%;
    background: var(--icon-bg);
    box-shadow: 0 0 0 6px var(--brown-deep);
    display: flex; align-items: center; justify-content: center;
  }
  .topic__title { font-weight: 700; font-size: 13.5px; line-height: 1.15; text-transform: uppercase; margin-bottom: 9px; }
  .topic__body { font-size: 10.5px; line-height: 1.36; color: var(--ink-soft); }

  .partners {
    position: absolute; left: 50px; top: 1062px;
    display: flex; gap: 26px; align-items: center;
  }
  .partner { color: var(--ink-white); font-weight: 600; font-size: 17px; line-height: 1.2; }
  .partner--belvorne { width: 130px; }
  .contact {
    position: absolute; left: 465px; top: 1068px;
    color: var(--ink-white); font-weight: 800; font-size: 36px; letter-spacing: 0.5px;
    white-space: nowrap;
  }
</style>
</head>
<body>
  <main class="flyer">
    <div class="hero-photo" role="img" aria-label="Portrait photo of Danielle and Ray Vorhagen smiling together in front of a brick building"></div>

    <svg class="leaders" width="900" height="1160" viewBox="0 0 900 1160" aria-hidden="true">
      <g stroke="rgba(255,255,255,0.7)" stroke-width="1" fill="none">
        <polyline points="118,252 118,295 152,330"/>
        <polyline points="808,357 808,405 772,438"/>
      </g>
      <circle cx="152" cy="330" r="4" fill="#fff" stroke="#4b3524" stroke-width="1.5"/>
      <circle cx="772" cy="438" r="4" fill="#fff" stroke="#4b3524" stroke-width="1.5"/>
    </svg>

    <div class="name-tag name-tag--left">Danielle Vorhagen</div>
    <div class="name-tag name-tag--right">Ray Vorhagen</div>

    <header class="headline">
      <h1 class="headline__kicker">ESTATE &amp; FINANCIAL PLANNING</h1>
      <div class="headline__main">ESSENTIALS</div>
    </header>

    <p class="perks">FOOD WILL BE PROVIDED | RAFFLE FOR $500 OFF AN ESTATE PLAN PACKAGE</p>

    <section class="topics">
      <article class="topic">
        <div class="topic__icon">
          <svg width="24" height="24" viewBox="0 0 24 24" fill="none" stroke="var(--icon-ink)" stroke-width="1.6">
            <circle cx="12" cy="9" r="6"/><path d="M6 9h12M12 3c2.5 3 2.5 9 0 12M12 3c-2.5 3-2.5 9 0 12"/>
            <path d="M3 17c3 0 5 1 7 3h7" stroke-linecap="round"/>
          </svg>
        </div>
        <h2 class="topic__title">Protect Your Future</h2>
        <p class="topic__body">Build a strong financial foundation with emergency funds, retirement planning, and smart investment strategies that match your goals.</p>
      </article>
      <article class="topic">
        <div class="topic__icon">
          <svg width="24" height="24" viewBox="0 0 24 24" fill="var(--icon-ink)">
            <path d="M12 2l8 3v6c0 5-3.5 9-8 11-4.5-2-8-6-8-11V5z"/>
            <path d="M8 12l3 3 5-6" fill="none" stroke="#fff" stroke-width="2" stroke-linecap="round" stroke-linejoin="round"/>
          </svg>
        </div>
        <h2 class="topic__title">Secure Your Legacy</h2>
        <p class="topic__body">Learn about wills, trusts, and powers of attorney - the essential documents everyone needs to protect their family's future.</p>
      </article>
      <article class="topic">
        <div class="topic__icon">
          <svg width="24" height="24" viewBox="0 0 24 24" fill="none" stroke="var(--icon-ink)" stroke-width="1.6">
            <rect x="6" y="3" width="12" height="8" rx="1"/><circle cx="12" cy="7" r="2"/>
            <path d="M3 16c3 0 5 1 7 3h8l3-3" stroke-linecap="round"/>
          </svg>
        </div>
        <h2 class="topic__title">Guard Your Assets</h2>
        <p class="topic__body">Understand the right insurance coverage to protect yourself and your loved ones, from life insurance to long-term care options.</p>
      </article>
      <article class="topic">
        <div class="topic__icon">
          <svg width="24" height="24" viewBox="0 0 24 24" fill="var(--icon-ink)">
            <path d="M9 3h6l-2 3h-2z"/>
            <path d="M10 7h4c4 3 6 7 6 10a4 4 0 0 1-4 4H8a4 4 0 0 1-4-4c0-3 2-7 6-10z"/>
            <text x="12" y="18" font-family="Montserrat, sans-serif" font-size="9" font-weight="700" fill="#fff" text-anchor="middle">$</text>
          </svg>
        </div>
        <h2 class="topic__title">Transfer Wealth Wisely</h2>
        <p class="topic__body">Discover tax-efficient strategies for passing assets to the next generation and making the most of your charitable giving.</p>
      </article>
    </section>

    <footer>
      <div class="partners">
        <span class="partner partner--belvorne">Belvorne Financial Planning</span>
        <span class="partner">PMR Law</span>
      </div>
      <div class="contact">YOUR CONTCAT</div>
    </footer>
  </main>
</body>
</html>
```